Business Card Design Project

We need a business card design for an existing company in Dallas/Fort Worth that is expanding services and re-branding. We are changing the name from Brightmoor Commercial Cleaning to Keystride Facility Services. We are expanding from only commercial cleaning to include complete commercial landscape and facility maintenance services, too.

As stated, we offer a package of services that includes landscape, janitorial and facility services, which is largely unique in the industry.

We would like a design that communicates trust/partnership with a professional, corporate image, but not necessarily using the standard white business card. We would like a design that perhaps uses darker blues or perhaps a gray background, but we are open to other ideas. We might also be interested in a double-sided design - maybe with our logo on the back, printed on a gray background?

We will probably stick with the attached logo, but if you've got another inspired idea....

Target Market(s)

Property managers, commercial real estate professionals, corporate executives

Industry/Entity Type

Landscape

Requirements
Should not have
• Not interested in old style fonts.

```html
<!DOCTYPE html>
<html lang="en">
<head>
<meta charset="utf-8">
<title>Keystride Facility Services – Business Card</title>
<link href="https://fonts.googleapis.com/css2?family=Lato:ital,wght@0,400;0,700;1,400&display=swap" rel="stylesheet">
<style>
  :root {
    --backdrop: #dfe4e6;
    --card-front: #ffffff;
    --card-back: #9c9c9c;
    --ink: #2b2b2b;
    --ink-soft: #555555;
    --ink-muted: #8a8a8a;
    --rule: #d4d4d4;
    --shadow: rgba(30, 45, 55, 0.22);
  }
  * { box-sizing: border-box; margin: 0; padding: 0; }
  html, body {
    width: 1200px; height: 960px; overflow: hidden;
    background: var(--backdrop);
    font-family: "Lato", sans-serif;
    color: var(--ink);
  }
  .canvas {
    width: 1200px; height: 960px;
    display: flex; flex-direction: column; align-items: center; justify-content: center;
    gap: 56px;
  }
  .card {
    width: 700px; height: 400px;
    position: relative;
    box-shadow: 0 14px 34px var(--shadow);
  }
  /* Front */
  .card-front { background: var(--card-front); }
  .brand {
    position: absolute; top: 44px; left: 0; right: 0;
    display: flex; justify-content: center;
  }
  .brand-row { display: flex; align-items: center; gap: 14px; }
  .brand-mark {
    flex: none;
    width: 76px; height: 76px; border: 5px solid var(--ink);
  }
  .brand-text { display: flex; flex-direction: column; }
  .brand-name {
    font-size: 32px; font-weight: 400; letter-spacing: 3px;
    text-transform: uppercase; color: var(--ink);
    line-height: 1.1; white-space: nowrap;
  }
  .brand-name span { display: block; }
  .tagline {
    margin-top: 4px;
    font-size: 12px; font-style: italic; color: var(--ink-soft);
    white-space: nowrap;
  }
  .person {
    position: absolute; top: 196px; left: 0; right: 0; text-align: center;
  }
  .person-name { font-size: 28px; color: var(--ink); }
  .person-title { font-size: 16px; color: var(--ink-soft); margin-top: 4px; }
  .divider {
    position: absolute; top: 286px; left: 70px; right: 70px; height: 1px;
    background: linear-gradient(90deg, transparent, var(--rule) 20%, var(--rule) 80%, transparent);
  }
  .contact {
    position: absolute; top: 304px; left: 0; right: 0; text-align: center;
    font-size: 18px; color: var(--ink);
  }
  .contact-line { display: flex; justify-content: center; align-items: center; gap: 30px; }
  .contact-item { display: flex; align-items: center; gap: 10px; }
  .contact-item svg { width: 16px; height: 16px; fill: var(--ink-muted); }
  .address { margin-top: 12px; }
  /* Back */
  .card-back {
    background: var(--card-back);
    display: flex; flex-direction: column; align-items: center; justify-content: center;
  }
  .back-mark {
    width: 150px; height: 120px; border: 8px solid var(--ink);
  }
  .back-name {
    margin-top: 26px; font-size: 26px; letter-spacing: 3px;
    text-transform: uppercase; color: var(--ink);
  }
  .website {
    margin-top: 22px; font-size: 16px; letter-spacing: 1px; color: var(--ink);
  }
</style>
</head>
<body>
  <main class="canvas">
    <section class="card card-front" aria-label="Business card front">
      <div class="brand">
        <div class="brand-row">
          <div class="brand-mark"></div>
          <div class="brand-text">
            <div class="brand-name"><span>Keystride</span><span>Facility Services</span></div>
            <p class="tagline">One Source For Landscape, Janitorial and Facility Maintenance</p>
          </div>
        </div>
      </div>
      <div class="person">
        <p class="person-name">Helena Marsh</p>
        <p class="person-title">Director</p>
      </div>
      <div class="divider"></div>
      <div class="contact">
        <div class="contact-line">
          <span class="contact-item">
            <svg viewBox="0 0 24 24" aria-label="Phone"><path d="M6.6 10.8a15 15 0 0 0 6.6 6.6l2.2-2.2c.3-.3.7-.4 1-.2 1.1.4 2.3.6 3.6.6.6 0 1 .4 1 1V20c0 .6-.4 1-1 1A17 17 0 0 1 3 4c0-.6.4-1 1-1h3.5c.6 0 1 .4 1 1 0 1.3.2 2.5.6 3.6.1.3 0 .7-.2 1l-2.3 2.2z"/></svg>
            216-555-0148
          </span>
          <span class="contact-item">
            <svg viewBox="0 0 24 24" aria-label="Fax"><path d="M7 3h10v5H7zM4 9h16a1 1 0 0 1 1 1v8h-4v3H7v-3H3v-8a1 1 0 0 1 1-1zm5 7v3h6v-3z"/></svg>
            216-555-0148
          </span>
        </div>
        <p class="address">Level 3, 41 Harrow Street, PO Box 2260, Auckland 1150</p>
      </div>
    </section>

    <section class="card card-back" aria-label="Business card back">
      <div class="back-mark"></div>
      <p class="back-name">Keystride Facility Services</p>
      <p class="website">www.keystridefacility.com</p>
    </section>
  </main>
</body>
</html>
```